Harbor Crest Industrial Services Brochure

-Need a tri-fold brochure, please use our new website colors and theme (I will attach a screen shot as it not live yet).
- Same layout as old brochure will work but I want to match our new website design (I will attach).
-I have attached our old brochure with pen written edits
-We need to add a valve section, if you can find a better image similar to what I attache that would be great.
-I want to replace the BOP stack image with some large refiner tank image, they are usually white tanks. Ill attached a sample picture.
-I will like to replace the front cover spray gun image with sandblaster balsting the 2 large pipes.
-you can use other same images or find good replacments but they have express a fresh paint job.
-Replace structual picture with yellow/orange frame picture attached
Updates
Also add Oven Cured Coatings to Surface Coating section.
Target Market(s)
Industrial customers
Industry/Entity Type
oil & gas, refinery, heavy equipment
Look and feel

```html
<!DOCTYPE html>
<html lang="en">
<head>
<meta charset="utf-8">
<title>Harbor Crest Industrial Services – Tri-fold Brochure</title>
<link rel="stylesheet" href="https://fonts.googleapis.com/css2?family=Oswald:wght@500;600&family=Roboto+Condensed:wght@300;400;700&display=swap">
<style>
  :root{
    --blue:#1560b7;
    --blue-dark:#0f4f9c;
    --charcoal:#3d3e42;
    --ink:#4a4c52;
    --white:#ffffff;
    --backdrop:#9b9b9b;
    --sky:#dfe8f2;
  }
  *{box-sizing:border-box;margin:0;padding:0}
  html,body{width:1018px;height:1200px;overflow:hidden;background:var(--backdrop)}
  .canvas{position:relative;width:1018px;height:1200px;overflow:hidden;background:var(--backdrop);font-family:"Roboto Condensed",Arial,sans-serif}
  .sheet{position:absolute;left:152px;width:715px;height:505px;background:var(--white);box-shadow:0 12px 18px rgba(0,0,0,.28)}
  .sheet--outside{top:77px}
  .sheet--inside{top:617px}
  .panel{position:absolute;top:0;width:238px;height:505px;overflow:hidden}
  .panel--1{left:0}
  .panel--2{left:238px}
  .panel--3{left:477px;width:238px}

  .heading{position:absolute;height:31px;background:var(--blue);color:var(--white);
    font-family:"Oswald",Arial,sans-serif;font-weight:500;font-size:15px;letter-spacing:-.2px;
    line-height:31px;padding-left:24px;clip-path:polygon(0 0,100% 0,calc(100% - 12px) 100%,0 100%)}
  .heading--dark{background:var(--charcoal);padding-left:11px}
  .accent{position:absolute;height:31px;background:var(--charcoal);clip-path:polygon(14px 0,100% 0,100% 100%,0 100%)}
  .accent--white{background:var(--white)}

  .checklist{list-style:none;position:absolute}
  .checklist li{position:relative;padding-left:17px;font-weight:300;font-size:14px;line-height:20.4px;color:var(--ink)}
  .checklist li::before{content:"";position:absolute;left:0;top:5px;width:11px;height:11px;border:1.6px solid var(--blue)}
  .checklist li::after{content:"";position:absolute;left:3.5px;top:5px;width:4px;height:7px;border:solid var(--blue);border-width:0 2px 2px 0;transform:rotate(40deg)}
  .checklist--light li{color:var(--white);font-size:14px}
  .checklist--light li::before{border-color:var(--white)}
  .checklist--light li::after{border-color:var(--white)}

  .photo{position:absolute}

  /* outside sheet */
  .coatings-list{left:25px;top:52px}
  .painter-photo{left:0;top:268px;width:238px;height:237px;background:linear-gradient(180deg,rgba(255,255,255,0) 0%,#d9dee6 40%,#b9c4d3 100%)}
  .cert-card{position:absolute;left:94px;top:395px;width:125px;height:90px;background:var(--white);border-radius:12px;box-shadow:0 2px 6px rgba(0,0,0,.25)}
  .cert-card .badge{position:absolute;left:16px;width:93px;height:22px;border-radius:4px;background:#c9d3e0}
  .cert-card .badge--top{top:13px}
  .cert-card .badge--bottom{top:50px;background:#d6dbe2}

  .blast-photo{left:0;top:0;width:238px;height:150px;background:linear-gradient(160deg,#8c97a3 0%,#b4bcc6 45%,#6f86a8 100%)}
  .facility{position:absolute;left:0;top:150px;width:238px;height:355px;background:var(--blue)}
  .facility .heading{top:0;width:196px}
  .facility .accent--white{top:0;left:200px;width:38px}
  .facility .heading--coating{top:181px;width:196px;padding-left:20px}
  .facility .accent--coating{top:181px}
  .prep-list{left:14px;top:46px}
  .prep-list li{line-height:17.4px;margin-bottom:10px}
  .coat-list{left:14px;top:224px}

  .brand{position:absolute;left:0;width:238px;text-align:center}
  .brand__mark{display:inline-block;width:14px;height:14px;background:var(--blue);margin-bottom:8px}
  .brand__name{font-family:"Oswald",Arial,sans-serif;font-weight:600;color:var(--blue);line-height:1.15}
  .brand--cover{top:46px}
  .brand--cover .brand__name{font-size:23px}
  .pipes-photo{left:0;top:222px;width:238px;height:283px;background:linear-gradient(180deg,rgba(255,255,255,0) 0%,#e6e3df 25%,#cfc4b7 65%,#a99b8a 100%)}
  .web-bar{position:absolute;left:43px;top:472px;width:195px;height:33px;background:var(--blue);color:var(--white);
    font-family:"Oswald",Arial,sans-serif;font-weight:500;font-size:16px;line-height:33px;text-align:right;padding-right:14px;
    clip-path:polygon(12px 0,100% 0,100% 100%,0 100%)}
  .web-accent{position:absolute;left:0;top:472px;width:50px;height:33px;background:var(--charcoal);clip-path:polygon(0 0,60% 0,30% 100%,0 100%)}

  /* inside sheet */
  .industries{background:linear-gradient(180deg,#ffffff 0%,#f2f4f7 55%,#e3e8ef 100%)}
  .industries-list{left:19px;top:47px}
  .brand--inside{top:236px;left:90px;width:130px}
  .brand--inside .brand__name{font-size:15px}
  .tanks-photo{left:0;top:272px;width:238px;height:233px;background:linear-gradient(180deg,rgba(226,232,240,0) 0%,#e9ecef 30%,#d2d7dc 75%,#b7bdc2 100%)}
  .photo-tag{position:absolute;height:22px;background:var(--blue);color:var(--white);font-family:"Oswald",Arial,sans-serif;font-weight:500;font-size:13px;line-height:22px;padding-left:11px}
  .tanks-tag{left:175px;top:483px;width:63px;padding-left:6px;clip-path:polygon(8px 0,100% 0,100% 100%,0 100%)}

  .gallery{background:var(--charcoal)}
  .gallery__item{position:absolute;left:13px;width:213px;height:105px}
  .gallery__item .photo-tag{left:0;bottom:0;width:133px;clip-path:polygon(0 0,calc(100% - 12px) 0,100% 100%,0 100%)}
  .gallery__item--structural{top:10px;background:linear-gradient(180deg,#b9c6cc 0%,#e8ecee 50%,#8a8f93 100%)}
  .gallery__item--assemblies{top:136px;background:linear-gradient(135deg,#2f5fae 0%,#1f4b97 50%,#5a7fbd 100%)}
  .gallery__item--equipment{top:262px;background:linear-gradient(180deg,#c9d5c7 0%,#b83030 40%,#8e2222 75%,#3a3a3a 100%)}
  .gallery__item--valves{top:386px;background:linear-gradient(160deg,#cfd3d6 0%,#8f969c 50%,#c9c1b2 100%)}

  .frame-photo{left:0;top:0;width:238px;height:216px;background:linear-gradient(180deg,#c8d8ea 0%,#dce6f0 35%,#e49b3a 60%,#c9c6c0 100%)}
  .lift-title{position:absolute;right:24px;top:19px;text-align:right;font-family:"Oswald",Arial,sans-serif;font-weight:500;font-size:17px;line-height:20px;color:var(--blue)}
  .service .heading{left:0;width:203px;padding-left:16px}
  .service .accent{left:214px;width:24px}
  .h-inhouse{top:217px}
  .h-access{top:307px}
  .h-quote{top:397px}
  .inhouse-list{left:17px;top:256px}
  .inhouse-list li,.access-list li{font-size:14px;line-height:18px}
  .access-list{left:17px;top:346px}
  .access-list .inline{display:inline-block;position:relative;padding-left:17px;margin-left:5px}
  .access-list .inline::before{content:"";position:absolute;left:0;top:5px;width:11px;height:11px;border:1.6px solid var(--blue)}
  .access-list .inline::after{content:"";position:absolute;left:3.5px;top:5px;width:4px;height:7px;border:solid var(--blue);border-width:0 2px 2px 0;transform:rotate(40deg)}
  .contact{position:absolute;left:12px;top:437px;list-style:none}
  .contact li{display:flex;align-items:center;gap:6px;font-size:14px;font-weight:300;line-height:17.5px;color:var(--ink)}
  .contact svg{width:12px;height:12px;flex:none}
  .contact strong{font-weight:700}
</style>
</head>
<body>
<div class="canvas">

  <!-- outside -->
  <section class="sheet sheet--outside">
    <div class="panel panel--1">
      <div class="heading" style="top:0;left:0;width:183px">SURFACE COATINGS</div>
      <div class="accent" style="top:0;left:193px;width:45px"></div>
      <ul class="checklist coatings-list">
        <li>Epoxy Coatings</li><li>Urethane Coatings</li><li>Zinc Primers</li><li>Tank Linings</li>
        <li>Non-Skid Coatings</li><li>High Temp Coatings</li><li>Floor Coatings</li><li>Fireproof Coatings</li>
        <li>Polyurea</li><li>Powder Coating</li><li>Oven Cured Coatings</li>
      </ul>
      <div class="photo painter-photo" role="img" aria-label="Worker in white protective suit spray painting a large steel surface"></div>
      <div class="cert-card" role="img" aria-label="Quality certification and inspector accreditation badges">
        <span class="badge badge--top"></span><span class="badge badge--bottom"></span>
      </div>
    </div>

    <div class="panel panel--2">
      <div class="photo blast-photo" role="img" aria-label="Blaster in protective hood working on steel beams inside a blast enclosure"></div>
      <div class="facility">
        <div class="heading heading--dark">SURFACE PREPARATION AREAS</div>
        <div class="accent accent--white"></div>
        <ul class="checklist checklist--light prep-list">
          <li>1-Blast Enclosure<br>75'Wx60' Lx28'H<br>(4,500sqft).</li>
          <li>5+ Acres of Outdoor Blast<br>Area for items in excess of<br>75'in Length or Width</li>
        </ul>
        <div class="heading heading--dark heading--coating">COATING AREAS</div>
        <div class="accent accent--white accent--coating" style="left:200px;width:38px"></div>
        <ul class="checklist checklist--light coat-list">
          <li>1- Large Spray Booth 50' x 120'</li>
          <li>2- Large Spray Booths 75' x 60'</li>
          <li>1- Mid Size Booth 35' x 30'</li>
          <li>20,000 sqft of Total Coating Booth</li>
          <li>7 acres of Laydown Yard</li>
        </ul>
      </div>
    </div>

    <div class="panel panel--3">
      <div class="brand brand--cover">
        <span class="brand__mark"></span>
        <p class="brand__name">Harbor Crest<br>Industrial Services</p>
      </div>
      <div class="photo pipes-photo" role="img" aria-label="Sandblaster blasting the inside of two large steel pipes"></div>
      <div class="web-accent"></div>
      <div class="web-bar">HARBORCRESTINC.COM</div>
    </div>
  </section>

  <!-- inside -->
  <section class="sheet sheet--inside">
    <div class="panel panel--1 industries">
      <div class="heading" style="top:0;left:0;width:183px;padding-left:18px">INDUSTRIES WE SERVE</div>
      <div class="accent" style="top:0;left:193px;width:45px"></div>
      <ul class="checklist industries-list">
        <li>Structural Steel</li><li>Critical components</li><li>Processing &amp; Refining</li><li>Waste Management</li>
        <li>Subsea Structures</li><li>Skid Packages</li><li>Heavy Equipment</li><li>Transportation</li>
        <li>Tanks</li><li>Valves</li>
      </ul>
      <div class="photo tanks-photo" role="img" aria-label="Large white refinery storage tanks with stairways"></div>
      <div class="brand brand--inside">
        <span class="brand__mark"></span>
        <p class="brand__name">Harbor Crest<br>Industrial Services</p>
      </div>
      <div class="photo-tag tanks-tag">TANKS</div>
    </div>

    <div class="panel panel--2 gallery">
      <div class="gallery__item gallery__item--structural" role="img" aria-label="Freshly painted white structural steel on a flatbed truck">
        <span class="photo-tag">STRUCTURAL</span></div>
      <div class="gallery__item gallery__item--assemblies" role="img" aria-label="Row of blue painted motor assemblies">
        <span class="photo-tag">ASSEMBLIES</span></div>
      <div class="gallery__item gallery__item--equipment" role="img" aria-label="Red painted heavy transport trailer with many wheels">
        <span class="photo-tag">HEAVY EQUIPMENT</span></div>
      <div class="gallery__item gallery__item--valves" role="img" aria-label="Rows of grey coated industrial valves on pallets">
        <span class="photo-tag">VALVES</span></div>
    </div>

    <div class="panel panel--3 service">
      <div class="photo frame-photo" role="img" aria-label="Large orange painted steel frame in a yard with a forklift"></div>
      <p class="lift-title">LIFTING CAPACITY OF<br>125,000 LBS</p>

      <div class="heading h-inhouse">INHOUSE &amp; FIELD SERVICES</div>
      <div class="accent h-inhouse"></div>
      <ul class="checklist inhouse-list">
        <li>24 hours a day, 7 days a week</li>
        <li>Mobile equipment on standby</li>
      </ul>

      <div class="heading h-access">EASY ACCES TO</div>
      <div class="accent h-access"></div>
      <ul class="checklist access-list">
        <li>Beltway 8 <span class="inline">Houston Ports</span></li>
        <li>Jfk and Hobby Airports</li>
      </ul>

      <div class="heading h-quote">NEED A QUOTE?</div>
      <div class="accent h-quote"></div>
      <ul class="contact">
        <li><svg viewBox="0 0 12 12"><path d="M6 0.5a4 4 0 0 0-4 4c0 3 4 7 4 7s4-4 4-7a4 4 0 0 0-4-4z" fill="#1560b7"/><circle cx="6" cy="4.5" r="1.5" fill="#fff"/></svg>2480 Ridgeline Rd, Houston, TX 77044</li>
        <li><svg viewBox="0 0 12 12"><path d="M2.5 1l2 2.2-1 1.3a7 7 0 0 0 4 4l1.3-1 2.2 2-1.2 1.5C5.5 11 1 6.5 1 2.2z" fill="#1560b7"/></svg>Office : <strong>281-555-0147</strong></li>
        <li><svg viewBox="0 0 12 12"><rect x="0.5" y="2" width="11" height="8" fill="#1560b7"/><path d="M0.5 2.5l5.5 4 5.5-4" fill="none" stroke="#fff" stroke-width="1"/></svg>quotes@harborcrestinc.com</li>
      </ul>
    </div>
  </section>

</div>
</body>
</html>
```